Im open to ideas.. I was thinking on my business cards aswell as my logo. a place for my name. email. phone number and abn..

ive attched a file with my business logo. which i dont love the colours.. i was think a dark background with charcoal letters so something along those colour schumes but im open to ideas..

Industry/Entity Type

Business

Logo Text

RLB Constructions

```html
<!DOCTYPE html>
<html lang="en">
<head>
<meta charset="UTF-8">
<title>RLB Constructions – Business Card</title>
<link rel="stylesheet" href="https://fonts.googleapis.com/css2?family=Roboto:wght@400;500;700&display=swap">
<style>
  :root {
    --stage: #3b4045;
    --card: #eef0f1;
    --card-edge: #dfe3e5;
    --ink: #1d1d1f;
    --muted: #555a5e;
    --red: #b3262b;
    --red-deep: #8e1b1f;
    --band-dark: #1e1f21;
  }
  * { box-sizing: border-box; margin: 0; padding: 0; }
  html, body {
    width: 1200px;
    height: 970px;
    overflow: hidden;
    background: var(--stage);
    font-family: "Roboto", Arial, sans-serif;
  }
  .card {
    position: absolute;
    left: 120px;
    top: 198px;
    width: 960px;
    height: 574px;
    background: linear-gradient(160deg, #f6f7f8 0%, var(--card) 55%, var(--card-edge) 100%);
    border: 1px solid #d4d8da;
    overflow: hidden;
  }
  .brand {
    position: absolute;
    left: 0;
    right: 0;
    top: 160px;
    text-align: center;
    font-weight: 700;
    font-size: 64px;
    letter-spacing: 1px;
    color: var(--ink);
    line-height: 1;
  }
  .contact {
    position: absolute;
    left: 60px;
    top: 344px;
  }
  .contact-line {
    display: flex;
    align-items: center;
    gap: 12px;
    font-size: 21px;
    color: var(--muted);
    height: 30px;
    margin-bottom: 14px;
  }
  .contact-line svg { width: 22px; height: 22px; flex: none; }
  .address {
    margin-top: 12px;
    font-size: 26px;
    font-weight: 700;
    color: var(--red);
    line-height: 33px;
  }
  .person {
    position: absolute;
    right: 52px;
    top: 380px;
    text-align: right;
  }
  .person-name {
    font-size: 30px;
    font-weight: 700;
    color: var(--red-deep);
    line-height: 36px;
  }
  .person-role {
    font-size: 19px;
    color: var(--ink);
    line-height: 24px;
  }
  .person-web {
    margin-top: 16px;
    font-size: 24px;
    font-weight: 700;
    color: var(--red);
  }
  .base-bands {
    position: absolute;
    left: 0;
    bottom: 0;
    width: 960px;
    height: 30px;
  }
</style>
</head>
<body>
  <div class="card">
    <div class="brand">RLB Constructions</div>

    <div class="contact">
      <div class="contact-line">
        <svg viewBox="0 0 24 24" aria-hidden="true"><path fill="var(--red)" d="M4 9c0-3 3-5 8-5s8 2 8 5v2h-4V9c-1-1-7-1-8 0v2H4zM6 12h12l2 8H4z"/></svg>
        <span>0400555019</span>
      </div>
      <div class="contact-line">
        <svg viewBox="0 0 24 24" aria-hidden="true"><rect x="2" y="5" width="20" height="14" fill="var(--red)"/><path d="M2 5l10 8 10-8" fill="none" stroke="#fff" stroke-width="1.8"/></svg>
        <span>info@rlbconstructions.com</span>
      </div>
      <div class="address">48 harbor 17th<br>Seaview park ny 10021</div>
    </div>

    <div class="person">
      <div class="person-name">Daniel Harker</div>
      <div class="person-role">Owner / Founder</div>
      <div class="person-web">www.rlbconstructions.com</div>
    </div>

    <svg class="base-bands" viewBox="0 0 960 30" preserveAspectRatio="none" aria-hidden="true">
      <defs>
        <linearGradient id="band-red" x1="0" x2="1">
          <stop offset="0" stop-color="#d12e33"/>
          <stop offset="1" stop-color="#8e1b1f"/>
        </linearGradient>
      </defs>
      <rect x="0" y="8" width="580" height="22" fill="var(--band-dark)"/>
      <path d="M572 30 Q584 4 612 4 L960 4 L960 30 Z" fill="url(#band-red)"/>
    </svg>
  </div>
</body>
</html>
```